Beauty website banner

We are an Australian beauty website selling mid and high end cosmetics and beauty products.

We need a banner that tells customers they can share their product wishlists with friends to let them know what they want for Christmas.

Target Market(s)

Female, 30-60, white collar

Industry/Entity Type

Cosmetics

Requirements
Must have
• 600 x 150 pixels in size

Words to be as follows, not including the (") of course.

"Share your wishlist with friends and family for Christmas!"

(Then in smaller font) "Just log in to your account, go to your wishlist and click on the ‘share wishlist’ button"

```html
<!DOCTYPE html>
<html lang="en">
<head>
<meta charset="utf-8">
<title>Share your wishlist for Christmas</title>
<link rel="stylesheet" href="https://fonts.googleapis.com/css2?family=Courgette&family=Open+Sans:wght@400;600&display=swap">
<style>
  :root {
    --sky-top: #3da6e6;
    --sky-mid: #47ade9;
    --sky-light: #8fcdf2;
    --snow: #ffffff;
    --text: #ffffff;
  }
  html, body {
    margin: 0;
    padding: 0;
    width: 1200px;
    height: 300px;
    overflow: hidden;
    background: var(--snow);
  }
  .banner {
    position: relative;
    width: 1200px;
    height: 300px;
    overflow: hidden;
    background:
      linear-gradient(180deg, var(--sky-top) 0%, var(--sky-mid) 55%, var(--sky-light) 78%, var(--snow) 100%);
  }
  .snow-drift {
    position: absolute;
    left: 0;
    bottom: 0;
    width: 1200px;
    height: 110px;
    background:
      radial-gradient(ellipse 420px 70px at 20% 100%, rgba(255,255,255,0.95), rgba(255,255,255,0) 100%),
      radial-gradient(ellipse 520px 80px at 75% 100%, rgba(255,255,255,0.95), rgba(255,255,255,0) 100%);
  }
  .snowflakes {
    position: absolute;
    inset: 0;
  }
  .snowflakes .flake-zone {
    position: absolute;
    border-radius: 50%;
    background: radial-gradient(circle, rgba(255,255,255,0.55) 0%, rgba(255,255,255,0) 70%);
  }
  .zone-top-left { left: 20px; top: 0; width: 120px; height: 90px; }
  .zone-left { left: 0; top: 170px; width: 110px; height: 130px; }
  .zone-top-right { right: 0; top: 0; width: 200px; height: 140px; }
  .zone-bottom-right { right: 20px; bottom: 0; width: 160px; height: 80px; }
  .message {
    position: absolute;
    left: 0;
    top: 0;
    width: 1200px;
    text-align: center;
    color: var(--text);
  }
  .headline {
    margin: 0;
    position: absolute;
    top: 58px;
    left: 0;
    width: 1200px;
    font-family: "Courgette", cursive;
    font-weight: 400;
    font-size: 54px;
    line-height: 62px;
    letter-spacing: 0.5px;
    text-shadow: 0 1px 3px rgba(20, 90, 150, 0.25);
  }
  .instructions {
    margin: 0;
    position: absolute;
    top: 196px;
    left: 150px;
    width: 910px;
    font-family: "Open Sans", Arial, sans-serif;
    font-weight: 400;
    font-size: 19.5px;
    line-height: 24px;
    white-space: nowrap;
    text-align: left;
  }
</style>
</head>
<body>
  <div class="banner">
    <div class="snow-drift"></div>
    <div class="snowflakes" role="img" aria-label="Scattered white snowflake decorations around the banner edges">
      <div class="flake-zone zone-top-left"></div>
      <div class="flake-zone zone-left"></div>
      <div class="flake-zone zone-top-right"></div>
      <div class="flake-zone zone-bottom-right"></div>
    </div>
    <div class="message">
      <h1 class="headline">Share your wishlist with<br>friends and family for Christmas!</h1>
      <p class="instructions">Just log in to your account, go to your wishlist and click on the ‘Share wishlist’ button</p>
    </div>
  </div>
</body>
</html>
```